Web Design Project

The aim of this project to design a website for a service that would offer services for small business and non profit organizations using opensource software that is weaved to work together in harmony.

The website name is: velisto.net

Velisto in Arabic means: cabbage. Cabbage is composed of leaves, actually there is nothing except leaves. Each leave by itself is not called cabbage, but a collection of leaves that are organized in a central way would give us cabbage.

Same idea for Velisto where open source software very well organized and integrated would create a new thing with a new value.
Updates

Target Market(s)

Small business, Europe, Africa, Far east and Middle east

Industry/Entity Type

Small Business

Requirements
Must have
• The website would offer the following sections:
* Home page
* Benefits: value of velisto
* Applications: applications offered by velisto
* Pricing
* Purchase
* Customer log in
* Support
- FAQ
- Knowledge base
- Forums
- Open tickets

Please take the following consideration in design:
* White should predominate
* Only black and the colors of logo are permitted (attched)
Nice to have
• Design is better to express:
* Openness
* Dynamic
* Usable
* Cost effective

Files

```html
<!DOCTYPE html>
<html lang="en">
<head>
<meta charset="utf-8">
<title>Velisto – Creating a new thing with a new value</title>
<link href="https://fonts.googleapis.com/css2?family=Open+Sans:wght@300;400;600;700&family=Oswald:wght@500&family=Questrial&family=Arimo:wght@700&display=swap" rel="stylesheet">
<style>
  :root{
    --white:#ffffff;
    --ink:#222222;
    --grey-text:#555555;
    --grey-head:#7a726c;
    --rule:#cfc9c2;
    --green:#8cc92c;
    --green-dark:#6aa81e;
    --blue:#0a93dd;
    --yellow:#f6c300;
    --magenta:#b64b8e;
    --field:#f3f3f3;
    --field-border:#d6d6d6;
    --footer:#5e5e5e;
    --hero-deep:#06131f;
    --hero-mid:#0d3a58;
    --hero-glow:#2f8a2a;
  }
  *{margin:0;padding:0;box-sizing:border-box}
  html,body{width:1040px;height:1200px;overflow:hidden;background:var(--white)}
  body{font-family:"Open Sans",Arial,sans-serif;color:var(--grey-text)}
  .page{position:relative;width:980px;height:1125px;transform:scale(1.0612);transform-origin:0 0}
  .abs{position:absolute}

  /* header */
  .brand{left:18px;top:52px;display:flex;align-items:center;gap:10px}
  .brand-dot{width:26px;height:26px;border-radius:50%;background:var(--green)}
  .brand-name{font-family:"Questrial",Arial,sans-serif;font-size:32px;color:var(--ink);line-height:1}
  .tagline{right:26px;top:64px;font-family:"Questrial",Arial,sans-serif;font-size:26px;color:var(--ink)}
  .utility{right:28px;top:15px;display:flex;gap:10px}
  .utility a{display:flex;flex-direction:column;align-items:center;font-size:12px;color:var(--ink);text-decoration:none;font-family:Arial,sans-serif}
  .utility svg{height:16px;margin-bottom:3px}

  /* nav */
  .main-nav{left:0;top:111px;width:980px;height:28px;background:var(--green)}
  .main-nav a{position:absolute;top:0;height:28px;line-height:27px;font-family:"Arimo",Arial,sans-serif;font-weight:700;font-size:17px;color:var(--white);text-decoration:none;transform:translateX(-50%)}
  .main-nav .current{left:0;width:120px;background:var(--blue);text-align:center;transform:none}

  .hero{left:0;top:139px;width:980px;height:355px;
    background:radial-gradient(ellipse at 72% 70%, var(--hero-glow) 0%, transparent 35%),
               radial-gradient(ellipse at 40% 40%, var(--hero-mid) 0%, var(--hero-deep) 75%)}
  .band{left:0;top:494px;width:980px;height:70px;background:linear-gradient(#f3f5f0,#fff)}

  /* feature cards */
  .card{top:540px;width:301px;height:178px;color:var(--white);overflow:hidden;border-top:3px solid rgba(255,255,255,.25)}
  .card--support{left:16px;background:var(--yellow)}
  .card--apps{left:339px;background:var(--blue)}
  .card--kb{left:659px;background:var(--magenta)}
  .card h2{position:absolute;left:13px;top:20px;font-family:"Oswald",Arial,sans-serif;font-weight:500;font-size:27px;letter-spacing:-.3px;line-height:1}
  .card p{position:absolute;left:13px;top:60px;width:280px;font-size:12px;line-height:14.5px}
  .card .deco{position:absolute;right:14px;top:8px;opacity:.35}
  .btn-more{position:absolute;left:12px;top:128px;width:94px;height:24px;border-radius:12px;background:linear-gradient(#fff,#e6e6e6);border:1px solid #ccc;font-size:9.5px;font-weight:700;color:#6b6b6b;text-align:center;line-height:22px}

  /* columns */
  .col{top:775px;width:305px}
  .col-contact{left:12px}
  .col-news{left:337px}
  .col-testimonial{left:658px}
  .hatch{height:6px;background:repeating-linear-gradient(135deg,var(--rule) 0 2px,transparent 2px 5px)}
  .col-head{display:flex;align-items:center;gap:16px;height:48px;border-bottom:1px solid var(--rule)}
  .col-head h3{font-weight:400;font-size:24px;color:var(--grey-head);letter-spacing:.5px}

  .field{display:block;width:278px;height:28px;margin-bottom:6px;border:1px solid var(--field-border);border-radius:5px;background:var(--field);font-size:12.5px;color:#444;padding:6px 11px}
  .field--area{height:67px}
  .btn-send{width:72px;height:24px;border-radius:12px;background:linear-gradient(#9bd646,var(--green-dark));color:#fff;font-size:10px;font-weight:700;text-align:center;line-height:24px;margin-top:6px}

  .news-item{position:relative;height:100px}
  .news-thumb{position:absolute;left:2px;top:0;width:66px;height:66px;border:1px solid #ddd;padding:4px}
  .news-thumb div{width:100%;height:100%}
  .thumb-green{background:linear-gradient(135deg,#e6efdc,#7fbf3a)}
  .thumb-blue{background:linear-gradient(135deg,#d9eef9,#2a9fd8)}
  .news-date{position:absolute;left:82px;top:0;font-weight:700;font-size:14px;color:var(--blue)}
  .news-text{position:absolute;left:82px;top:22px;width:222px;font-size:12px;line-height:14.5px}

  .quote{position:relative;padding:30px 0 0 32px;font-size:12.5px;line-height:14.5px;color:#444}
  .quote-mark{position:absolute;left:0;top:22px;font-family:Georgia,serif;font-size:90px;line-height:1;color:#e3e8f0}
  .quote p{position:relative;margin-bottom:14px}
  .quote cite{position:relative;font-style:normal;font-weight:700;color:var(--blue)}

  .footer{left:0;top:1085px;width:980px;height:25px;background:var(--footer);color:#fff;font-size:11px;line-height:25px}
</style>
</head>
<body>
<div class="page">

  <header>
    <div class="abs brand"><span class="brand-dot"></span><span class="brand-name">velisto</span></div>
    <nav class="abs utility">
      <a href="#"><svg viewBox="0 0 18 14" width="20"><rect x="3" y="1" width="12" height="9" fill="#333"/><rect x="1" y="11" width="16" height="2" fill="#333"/></svg>login</a>
      <a href="#"><svg viewBox="0 0 14 16" width="14"><circle cx="7" cy="5" r="4" fill="#333"/><path d="M0 16 Q7 7 14 16Z" fill="#333"/></svg>support</a>
      <a href="#"><svg viewBox="0 0 10 16" width="10"><path d="M2 5 Q2 1 5 1 Q8 1 8 4 Q8 6 5 8 L5 10" stroke="#333" stroke-width="2.4" fill="none"/><rect x="3.8" y="12" width="2.4" height="2.4" fill="#333"/></svg>FAQ</a>
    </nav>
    <p class="abs tagline">Creating a new thing with a new value</p>
  </header>

  <nav class="abs main-nav">
    <a href="#" class="current">home</a>
    <a href="#" style="left:170px">benefits</a>
    <a href="#" style="left:302px">applications</a>
    <a href="#" style="left:430px">pricing</a>
    <a href="#" style="left:547px">purchase</a>
    <a href="#" style="left:703px">knowledge base</a>
    <a href="#" style="left:869px">open tickets</a>
  </nav>

  <div class="abs hero" role="img" aria-label="Photo of figures standing on glowing connected network nodes"></div>
  <div class="abs band"></div>

  <section class="abs card card--support">
    <svg class="deco" width="78" height="78" viewBox="0 0 78 78"><circle cx="39" cy="39" r="34" fill="none" stroke="#fff" stroke-width="7"/><text x="39" y="50" text-anchor="middle" font-family="Oswald, sans-serif" font-size="30" fill="#fff">24</text></svg>
    <h2>24/7 CLIENT SUPPORT</h2>
    <p>Lorem ipsum dolor sit amet, consectetuer adipiscing elit, sed diam nonummy nibh euismod tincidunt ut laoreet dolore magna.</p>
    <div class="btn-more">READ MORE</div>
  </section>
  <section class="abs card card--apps">
    <svg class="deco" width="70" height="70" viewBox="0 0 70 70"><path d="M10 10 L60 60 M60 10 L10 60" stroke="#fff" stroke-width="9" stroke-linecap="round"/></svg>
    <h2>APPLICATIONS</h2>
    <p>Duis autem vel eum iriure dolor in hendrerit in vulputate velit esse molestie consequat, vel illum dolore eu feugiat nulla facilisis at vero eros.</p>
    <div class="btn-more">READ MORE</div>
  </section>
  <section class="abs card card--kb">
    <svg class="deco" width="78" height="78" viewBox="0 0 78 78"><circle cx="39" cy="39" r="36" fill="#fff"/></svg>
    <h2>KNOWLEDGE BASE</h2>
    <p>Ut wisi enim ad minim veniam, quis nostrud exerci tation ullamcorper suscipit lobortis nisl ut aliquip ex ea commodo consequat.</p>
    <div class="btn-more">READ MORE</div>
  </section>

  <section class="abs col col-contact">
    <div class="hatch"></div>
    <div class="col-head">
      <svg width="30" height="32" viewBox="0 0 30 32"><circle cx="15" cy="10" r="7" fill="#7a726c"/><path d="M7 9 Q7 1 15 1 Q23 1 23 9" stroke="#6aa81e" stroke-width="2" fill="none"/><path d="M1 32 Q15 14 29 32Z" fill="#7a726c"/></svg>
      <h3>CONTACT US</h3>
    </div>
    <div style="margin-top:30px">
      <div class="field">Full Name</div>
      <div class="field">Email Address</div>
      <div class="field field--area">Message</div>
      <div class="btn-send">SEND</div>
    </div>
  </section>

  <section class="abs col col-news">
    <div class="hatch"></div>
    <div class="col-head">
      <svg width="24" height="26" viewBox="0 0 24 26"><rect x="1" y="4" width="22" height="21" rx="2" fill="none" stroke="#7a726c" stroke-width="2"/><rect x="1" y="4" width="22" height="6" fill="#7a726c"/><text x="12" y="22" text-anchor="middle" font-size="10" font-family="Arial, sans-serif" fill="#7a726c">15</text></svg>
      <h3>LATEST NEWS</h3>
    </div>
    <div style="margin-top:31px">
      <article class="news-item">
        <div class="news-thumb"><div class="thumb-green" role="img" aria-label="Illustration of a green arrow"></div></div>
        <p class="news-date">Fri, January. 03</p>
        <p class="news-text">Lorem ipsum dolor sit amet, consectet adipiscing elit, sed diam nonummy nibh euismod tincidunt ut .</p>
      </article>
      <article class="news-item">
        <div class="news-thumb"><div class="thumb-blue" role="img" aria-label="Illustration of a blue globe"></div></div>
        <p class="news-date">Mon, December. 28</p>
        <p class="news-text">Lorem ipsum dolor sit amet, consectet adipiscing elit, sed diam nonummy nibh euismod tincidunt ut .</p>
      </article>
    </div>
  </section>

  <section class="abs col col-testimonial">
    <div class="hatch"></div>
    <div class="col-head">
      <svg width="26" height="22" viewBox="0 0 26 22"><ellipse cx="13" cy="9" rx="12" ry="8" fill="#7a726c"/><path d="M6 15 L4 21 L12 16Z" fill="#7a726c"/></svg>
      <h3>TESTIMONIALS</h3>
    </div>
    <blockquote class="quote">
      <span class="quote-mark">&ldquo;</span>
      <p>Duis autem vel eum iriure dolor in hendrerit in vulputate velit esse molestie consequat, vel illum dolore eu feugiat nulla facilisis at vero eros et accumsan et iusto odio.</p>
      <p>Nam liber tempor cum soluta nobis eleifend option congue nihil imperdiet doming id quod mazim placerat facer possim assum.</p>
      <cite>mr. Aron Delmas (manager)</cite>
    </blockquote>
  </section>

  <footer class="abs footer">
    <span class="abs" style="left:310px">Copyright 2014. All rights reserved.</span>
    <span class="abs" style="left:517px">Privacy Policy | Terms of Use</span>
  </footer>

</div>
</body>
</html>
```